Financial Advisor Brochure to attract new clients

I am launching a new career as a Financial Advisor and a flier that shows what services I offer and why I decided to go back to work at this point in my life. I have a deep desire to help people meet their dreams and believe that a solid financial foundation provides the ability to live your life as you want to and not how you have to. I created a simple flier but know that so much more can be done to catch a persons eye.

Target Market(s)

Entrepeneurs and Woman in all stages of life.

Industry/Entity Type

Financial Advisor

Font styles to use
Sans Serif

Colors
00AB8E
00BBA5
67D7C9
C6EFE9
E9F9F6

Requirements
Must have
• my photo, contact information and Cobaltra Logo

```html
<!DOCTYPE html>
<html lang="en">
<head>
<meta charset="utf-8">
<title>Dana Verhoek – Financial Advisor Flyer</title>
<link href="https://fonts.googleapis.com/css2?family=Montserrat:wght@300;400;500;600;700;800&family=Oswald:wght@500;600&display=swap" rel="stylesheet">
<style>
:root{
  --stage:#c9cbce;
  --paper:#ffffff;
  --blue:#1d5e9e;
  --blue-bright:#2a73b8;
  --ink:#2b2b2b;
  --dark:#1b1b1b;
  --dark-soft:#3a3a3a;
  --muted:#9aa4ae;
  --white:#ffffff;
}
*{margin:0;padding:0;box-sizing:border-box}
html,body{width:1200px;height:2426px;overflow:hidden}
body{background:var(--stage);font-family:"Montserrat",Arial,sans-serif;position:relative}
.flyer{position:absolute;left:50px;top:501px;width:1020px;height:1320px;background:var(--paper);
  transform:scale(1.0784);transform-origin:0 0;box-shadow:0 18px 40px rgba(0,0,0,.25);overflow:hidden}
.backdrop{position:absolute;left:0;top:0;width:1020px;height:700px}
.abs{position:absolute}

.brand{left:45px;top:58px;display:flex;align-items:center;gap:14px}
.brand-dot{width:64px;height:64px;border-radius:50%;background:var(--blue)}
.brand-name{font-weight:600;color:var(--dark-soft);font-size:30px;letter-spacing:1.5px;line-height:1}
.brand-tag{left:124px;top:106px;font-size:11px;font-weight:700;letter-spacing:2.2px;color:var(--blue)}

.advisor{left:418px;top:182px;color:var(--white)}
.advisor-name{font-family:"Oswald",Arial,sans-serif;font-weight:600;font-size:48px;line-height:1;letter-spacing:.3px;padding-bottom:4px;border-bottom:2px solid var(--blue-bright);display:inline-block}
.advisor-role{font-weight:300;font-size:22px;letter-spacing:.5px;margin-top:2px}

.profile{left:48px;top:236px;width:400px;padding-left:13px;border-left:3px solid var(--white);color:var(--white)}
.profile h2{font-weight:800;font-size:36px;line-height:1.1}
.profile p{font-weight:400;font-size:18px;line-height:22px;margin-top:4px}

.appointment{left:47px;top:413px;background:var(--white);color:var(--dark);font-weight:800;font-size:21px;padding:3px 8px;border-radius:3px}
.phone{left:48px;top:453px;color:var(--white);font-weight:700;font-size:30px;display:flex;align-items:center;gap:8px;letter-spacing:1px}
.quick-contact{left:52px;top:496px;color:var(--white);font-size:14px;font-weight:600;line-height:21px}
.quick-contact div,.contact-list div{display:flex;align-items:center;gap:10px}

.story{left:48px;top:642px;width:420px;color:var(--ink);font-size:15.4px;line-height:18px}
.story p{margin-bottom:18px}

.contact-bar{left:0;top:1160px;width:360px;height:40px;background:linear-gradient(90deg,#111,#3b3b3b);color:var(--white);font-weight:800;font-size:22px;padding:5px 0 0 45px;box-shadow:0 3px 6px rgba(0,0,0,.3)}
.contact-list{left:45px;top:1217px;color:var(--dark);font-size:18px;font-weight:600;line-height:27px}

.services{left:528px;top:490px;width:445px;height:780px;background:var(--blue);border-radius:26px}
.services-head{left:604px;top:468px;width:292px;height:88px;background:linear-gradient(180deg,#2e2e2e,#151515);border-radius:0 0 14px 14px;color:var(--white);font-weight:800;font-size:22px;line-height:28px;text-align:center;padding-top:16px;box-shadow:0 4px 8px rgba(0,0,0,.35)}
.service{position:absolute;left:548px;width:410px;color:var(--white)}
.service-icon{position:absolute;left:0;top:2px;width:44px;height:44px;border-radius:50%;background:#1b1b1b;border:2px solid #fff;box-shadow:0 0 0 3px #1b1b1b}
.service-icon::after{content:"";position:absolute;left:11px;top:11px;width:18px;height:18px;border:2px solid #fff;border-radius:50%}
.service h3{margin-left:58px;font-weight:800;font-size:18px;line-height:22px}
.service ul{list-style:none;margin-left:76px;margin-top:4px}
.service li{position:relative;font-size:15.5px;line-height:18px;margin-bottom:5px;font-weight:500}
.service li::before{content:"";position:absolute;left:-17px;top:6px;width:7px;height:7px;border-radius:50%;background:var(--muted)}
.rule{position:absolute;left:548px;width:405px;border-top:1.5px dashed rgba(255,255,255,.75)}
</style>
</head>
<body>
<main class="flyer">
  <svg class="backdrop" viewBox="0 0 1020 700" aria-hidden="true">
    <defs>
      <linearGradient id="blueFade" x1="0" y1="0" x2="1" y2="0.3">
        <stop offset="0" stop-color="#2064a6"/>
        <stop offset=".55" stop-color="#174d84"/>
        <stop offset="1" stop-color="#0c2846"/>
      </linearGradient>
      <linearGradient id="darkFade" x1="0" y1="0" x2="1" y2="0">
        <stop offset="0" stop-color="#111"/>
        <stop offset="1" stop-color="#4a4a4a"/>
      </linearGradient>
      <linearGradient id="photoTone" x1="0" y1="0" x2="0" y2="1">
        <stop offset="0" stop-color="#6e4a33" stop-opacity=".85"/>
        <stop offset=".45" stop-color="#a9785a"/>
        <stop offset=".62" stop-color="#1f8f7c"/>
        <stop offset="1" stop-color="#147063"/>
      </linearGradient>
    </defs>
    <polygon points="0,135 700,320 790,390 180,595 0,560" fill="url(#blueFade)"/>
    <polygon points="0,525 190,592 0,630" fill="#0b0b0b"/>
    <polygon points="247,215 952,0 1020,0 1020,305 760,398 560,310" fill="url(#darkFade)"/>
    <g fill="#ffffff" opacity=".07">
      <rect x="330" y="420" width="8" height="120"/><rect x="350" y="400" width="8" height="140"/>
      <rect x="370" y="430" width="8" height="110"/><rect x="390" y="390" width="8" height="150"/>
      <rect x="410" y="370" width="8" height="170"/><rect x="430" y="405" width="8" height="135"/>
      <rect x="450" y="360" width="8" height="180"/><rect x="470" y="380" width="8" height="160"/>
      <rect x="490" y="340" width="8" height="200"/><rect x="510" y="355" width="8" height="185"/>
      <rect x="530" y="330" width="8" height="210"/><rect x="550" y="345" width="8" height="195"/>
      <rect x="570" y="320" width="8" height="220"/><rect x="590" y="335" width="8" height="205"/>
    </g>
    <g role="img" aria-label="Portrait photo of the financial advisor, smiling, in a teal blouse">
      <path d="M790,385 C770,300 775,230 800,200 C780,120 810,20 880,8 C950,0 995,60 990,150 C1000,200 1010,260 1000,310 L790,385 Z" fill="url(#photoTone)"/>
    </g>
  </svg>

  <div class="abs brand">
    <span class="brand-dot"></span>
    <span class="brand-name">COBALTRA ADVISORS</span>
  </div>
  <div class="abs brand-tag">GUIDANCE AT EVERY STAGE</div>

  <div class="abs advisor">
    <div class="advisor-name">DANA VERHOEK</div>
    <div class="advisor-role">FINANCIAL ADVISOR</div>
  </div>

  <section class="abs profile">
    <h2>PROFILE</h2>
    <p>Passionate about helping empower you with knowledge to make informed financial decisions throughout all of life’s stages to help you achieve your goals.</p>
  </section>

  <div class="abs appointment">CALL FOR AN APPOINTMENT</div>
  <div class="abs phone">
    <svg width="24" height="24" viewBox="0 0 24 24" aria-hidden="true"><circle cx="12" cy="12" r="11" fill="#fff"/><path d="M8 6.5l2 .2 1 3-1.4 1.2a7 7 0 0 0 3.5 3.5l1.2-1.4 3 1 .2 2c-4.8 1.3-10.8-4.7-9.5-9.5z" fill="#1d5e9e"/></svg>
    555-014-2368
  </div>
  <div class="abs quick-contact">
    <div><svg width="14" height="10" viewBox="0 0 14 10" aria-hidden="true"><rect width="14" height="10" fill="#fff"/><path d="M0 0l7 6 7-6" stroke="#1d5e9e" fill="none"/></svg>dana.verhoek@cobaltraadvisors.com</div>
    <div><svg width="14" height="14" viewBox="0 0 14 14" aria-hidden="true"><circle cx="7" cy="7" r="6" fill="none" stroke="#fff" stroke-width="1.6"/><path d="M1 7h12M7 1c-3 3-3 9 0 12M7 1c3 3 3 9 0 12" stroke="#fff" fill="none"/></svg>www.cobaltraadvisors.com</div>
  </div>

  <section class="abs story">
    <p>As a business owner, wife, and mother of two teenagers, I understand the struggles you face juggling your personal, business, and financial life.</p>
    <p>I grew up in a home where my parents had opposing money habits. My Dad was a big spender and mom was a saver. Through the years, I saw how my mom’s consistent savings grew while Dad’s style led to many financial ups and downs. This made a huge impression on me and sparked my continued interest in all things finance.</p>
    <p>Having an entrepreneurial personality and ability to explain concepts in a relatable manner has provided me with many opportunities. In 2018, After decades of running a sales agency, I sold my company to spend time with my kids and family but my interest in Finance never waned. Now that our kids are thriving teenagers, I started a new career as a licensed Financial Advisor with a heart to help you achieve your financial dreams.</p>
    <p>The financial world is changing rapidly, and it can be confusing on how to maneuver through these times. My goal is to pull out the emotions that cloud judgement and help you make better decisions with your long-range goals in mind.</p>
  </section>

  <div class="abs contact-bar">CONTACT INFORMATION</div>
  <div class="abs contact-list">
    <div><svg width="14" height="10" viewBox="0 0 14 10" aria-hidden="true"><rect width="14" height="10" fill="#1d5e9e"/><path d="M0 0l7 6 7-6" stroke="#fff" fill="none"/></svg>dana.verhoek@cobaltraadvisors.com</div>
    <div><svg width="14" height="14" viewBox="0 0 14 14" aria-hidden="true"><circle cx="7" cy="7" r="6" fill="none" stroke="#1d5e9e" stroke-width="1.6"/><path d="M1 7h12M7 1c-3 3-3 9 0 12M7 1c3 3 3 9 0 12" stroke="#1d5e9e" fill="none"/></svg>www.cobaltraadvisors.com</div>
  </div>

  <div class="abs services"></div>
  <div class="abs services-head">FINANCIAL PLANNING<br>SERVICES OFFERED</div>

  <div class="service" style="top:586px"><span class="service-icon"></span>
    <h3>TRANSITION PLANNING</h3>
    <ul><li>Divorce planning.</li><li>Strategy and guidance pre, during, and post- divorce</li></ul>
  </div>
  <div class="rule" style="top:697px"></div>
  <div class="service" style="top:717px"><span class="service-icon"></span>
    <h3>RETIREMENT PLANNING</h3>
    <ul><li>Current portfolio analysis</li><li>Timeline asset and income planning</li><li>Tax and estate review and projections</li></ul>
  </div>
  <div class="rule" style="top:828px"></div>
  <div class="service" style="top:847px"><span class="service-icon"></span>
    <h3>REAL ESTATE ACQUISITION OR SALE</h3>
    <ul><li>Acquisition or dissolution of real estate. Individual or portfolio</li></ul>
  </div>
  <div class="rule" style="top:926px"></div>
  <div class="service" style="top:940px"><span class="service-icon"></span>
    <h3>BUSINESS SALE OR PURCHASE</h3>
    <ul><li>Company valuations</li><li>Tax impact analysis</li><li>Strategy implementation for funds received from sale</li></ul>
  </div>
  <div class="rule" style="top:1062px"></div>
  <div class="service" style="top:1079px"><span class="service-icon"></span>
    <h3>ESTATE PLANNING</h3>
    <ul><li>Strategies for creating future generational wealth</li></ul>
  </div>
  <div class="rule" style="top:1155px"></div>
  <div class="service" style="top:1170px"><span class="service-icon"></span>
    <h3>NEW INVESTORS</h3>
    <ul><li>Assistance in opening investment and retirement acc</li></ul>
  </div>
</main>
</body>
</html>
```